New business card for my lawn and landscape business

Dorrin Yard and Building is a full-service lawn care, landscaping, and light construction company serving Paragould and the Northeast Arkansas region. The business is owned and operated by Marcus Toller, with a reputation for hands-on, detail-oriented service, dependable crews, and quality results for both residential and commercial clients. A well regarded business with great reviews.
Owner Marcus Toller
Dorrinyardandbuilding.example

Target Market(s)

Commercial, Middle, and upper class in north east Arkansas

Industry/Entity Type

Lawn maintenance and landscape

Contact Information for Business Card

Dorrin Yard And Building Professional lawn care, landscaping, and property improvement in Northeast Arkansas. • lawn maintenance •lawn treatments and weed control • exterior projects • Custom landscape design & installation • Sod, trees, rock & drainage solutions • Residential & commercial services Reliable. Detailed. Done right.

Requirements
Must have
• Business name, service area, list of some of our services, clean design that represents
Nice to have
• Unique. Different design element than just grass because its already in n the logo. Picture of a warm season (south) lawn or landscape. Pictures of the type of work we do

```html
<!DOCTYPE html>
<html lang="en">
<head>
<meta charset="utf-8">
<title>Dorrin Yard and Building – Business Card</title>
<link rel="stylesheet" href="https://fonts.googleapis.com/css2?family=Montserrat:wght@600&family=Arimo:wght@400;700&display=swap">
<style>
  :root {
    --page: #e6e6e6;
    --white: #ffffff;
    --green-top: #8cc152;
    --green-bottom: #76ad3e;
    --brand-green: #6aae3a;
    --emboss-green: #b9e08f;
    --divider: #8a8a8a;
    --ink-light: #ffffff;
  }
  * { box-sizing: border-box; margin: 0; padding: 0; }
  html, body { width: 1200px; height: 1200px; overflow: hidden; }
  body {
    background: var(--page);
    font-family: "Arimo", Arial, sans-serif;
    position: relative;
  }
  .card {
    position: absolute;
    left: 255px;
    width: 690px;
    height: 394px;
    border-radius: 20px;
    overflow: hidden;
  }
  .card--front { top: 160px; background: var(--white); }
  .card--back {
    top: 650px;
    background: linear-gradient(180deg, var(--green-top), var(--green-bottom));
  }

  /* Front */
  .front-brand {
    position: absolute;
    left: 0; top: 0;
    width: 316px; height: 100%;
    display: flex; align-items: center; justify-content: center; gap: 12px;
  }
  .brand-dot {
    width: 18px; height: 18px; border-radius: 50%;
    background: var(--brand-green);
    flex: none;
  }
  .brand-name {
    font-family: "Montserrat", Arial, sans-serif;
    font-weight: 600;
    font-size: 25px;
    line-height: 1.15;
    color: var(--brand-green);
  }
  .front-divider {
    position: absolute;
    left: 316px; top: 0;
    width: 8px; height: 100%;
    background: linear-gradient(90deg, #b5b5b5, var(--divider), #c9c9c9);
  }
  .front-panel {
    position: absolute;
    left: 324px; top: 0; right: 0; bottom: 0;
    background: linear-gradient(180deg, var(--green-top), var(--green-bottom));
    color: var(--ink-light);
  }
  .person-name {
    position: absolute;
    left: 32px; top: 122px;
    font-family: "Montserrat", Arial, sans-serif;
    font-weight: 600;
    font-size: 26px;
    letter-spacing: 1px;
  }
  .person-title {
    position: absolute;
    left: 32px; top: 155px;
    font-size: 16px;
  }
  .contact-list {
    position: absolute;
    left: 30px; top: 198px;
    list-style: none;
    font-size: 16px;
    line-height: 21px;
  }
  .contact-list li { display: flex; align-items: center; gap: 10px; }
  .contact-list svg { width: 14px; height: 14px; fill: var(--ink-light); flex: none; }

  /* Back */
  .back-brand {
    position: absolute;
    left: 60px; top: 150px;
    display: flex; align-items: center; gap: 12px;
  }
  .back-brand .brand-dot { background: var(--emboss-green); }
  .back-brand .brand-name { color: var(--emboss-green); font-size: 27px; }
  .back-copy {
    position: absolute;
    left: 347px; top: 66px; right: 20px;
    color: var(--ink-light);
  }
  .back-intro {
    font-weight: 700;
    font-size: 15.5px;
    line-height: 19px;
  }
  .service-list {
    list-style: none;
    margin-top: 8px;
    font-size: 15.5px;
    line-height: 23px;
  }
  .service-list li::before { content: "• "; }
  .tagline {
    margin-top: 14px;
    font-weight: 700;
    font-size: 16px;
  }
</style>
</head>
<body>

<section class="card card--front" aria-label="Business card front">
  <div class="front-brand">
    <span class="brand-dot"></span>
    <span class="brand-name">Dorrin Yard<br>&amp; Building</span>
  </div>
  <div class="front-divider"></div>
  <div class="front-panel">
    <h1 class="person-name">MARCUS TOLLER</h1>
    <p class="person-title">Owner</p>
    <ul class="contact-list">
      <li>
        <svg viewBox="0 0 24 24" aria-hidden="true"><path d="M6.6 10.8a15.1 15.1 0 0 0 6.6 6.6l2.2-2.2a1 1 0 0 1 1-.25 11.4 11.4 0 0 0 3.6.57 1 1 0 0 1 1 1V20a1 1 0 0 1-1 1A17 17 0 0 1 3 4a1 1 0 0 1 1-1h3.5a1 1 0 0 1 1 1c0 1.25.2 2.45.57 3.57a1 1 0 0 1-.25 1z"/></svg>
        736-555-0148
      </li>
      <li>
        <svg viewBox="0 0 24 24" aria-hidden="true"><path d="M2 5h20v14H2z M3 6l9 7 9-7" fill="none" stroke="#fff" stroke-width="0"/><path d="M2 5h20v2l-10 7L2 7z"/><path d="M2 9l10 7 10-7v10H2z"/></svg>
        info@Dorrinyardandbuilding.example
      </li>
      <li>
        <svg viewBox="0 0 24 24" aria-hidden="true"><circle cx="12" cy="12" r="10"/><path d="M7 8c2 0 3 1 3 3s2 2 2 4-1 3-1 5" stroke="#7fb547" stroke-width="2" fill="none"/></svg>
        www.Dorrinyardandbuilding.example
      </li>
    </ul>
  </div>
</section>

<section class="card card--back" aria-label="Business card back">
  <div class="back-brand">
    <span class="brand-dot"></span>
    <span class="brand-name">Dorrin Yard<br>&amp; Building</span>
  </div>
  <div class="back-copy">
    <p class="back-intro">Dorrin Yard &amp; Building<br>Professional lawn care, landscaping<br>&amp; property improvement in<br>Northeast Arkansas.</p>
    <ul class="service-list">
      <li>Lawn maintenance</li>
      <li>Lawn treatments &amp; weed control</li>
      <li>Exterior projects</li>
      <li>Custom landscape design &amp; installation</li>
      <li>Sod, trees, rock &amp; drainage solutions</li>
      <li>Residential &amp; commercial services</li>
    </ul>
    <p class="tagline">RELIABLE. DETAILED. DONE RIGHT</p>
  </div>
</section>

</body>
</html>
```